Vorlume is about building a community in the events space.

Looking to build Sildavora.com style website, with the following key features / functionality:
• Sign up / sign in page
• Profile pages - User / Speaker / Event Organiser
• Event categories and listings
• Ratings / Review Comments

Preferably for Wordpress platform, as in Wordpress plugin, with PHP access.

Target Market(s)

Event communities

Industry/Entity Type

Building

Coding

Coded - Design and coding required

Number of Pages Required

5+ page

Font styles to use
Sans Serif

Colors
0492cd

Requirements
Must have
• Vorlume is about building a community in the events space.
• Looking to build Sildavora.com style website, with the following key features / functionality:
• • Sign up / sign in page
• • Profile pages - User / Speaker / Event Organiser
• • Event categories and listings
• • Ratings / Review Comments
• Preferably for Wordpress platform, as in Wordpress plugin, with PHP access.

```html
<!DOCTYPE html>
<html lang="en">
<head>
<meta charset="utf-8">
<title>Vorlume – Events Community</title>
<link href="https://fonts.googleapis.com/css2?family=Ubuntu:wght@400;500&family=Open+Sans:wght@400;600&display=swap" rel="stylesheet">
<style>
:root{
  --brand:#0492cd;
  --brand-bright:#0aa2ef;
  --ink:#222;
  --text:#444;
  --muted:#b5b5b5;
  --line:#e3e3e3;
  --page:#f4f4f4;
  --white:#fff;
  --dark-btn:#3d3d3d;
  --footer:#e8e8e8;
}
*{box-sizing:border-box;margin:0;padding:0}
html,body{width:782px;height:1200px;overflow:hidden}
body{position:relative;background:var(--page);font-family:"Open Sans",sans-serif;color:var(--text)}
.abs{position:absolute}

/* header */
.site-header{position:absolute;left:0;top:0;width:782px;height:42px;background:var(--white)}
.brand-square{left:86px;top:0;width:42px;height:42px;background:var(--brand-bright)}
.brand-name{left:133px;top:9px;font-family:"Ubuntu",sans-serif;font-size:19px;color:var(--ink)}
.search{left:308px;top:10px;width:166px;height:23px;border:1px solid #ccc;background:#f7f7f7;font-size:7px;color:#555;padding:6px 9px}
.search svg{position:absolute;right:7px;top:7px}
.menu-btn{left:545px;top:9px;width:25px;height:25px;border:1px solid #ccc;border-radius:50%;background:#fff}
.menu-btn svg{position:absolute;left:7px;top:8px}
.btn{top:10px;height:23px;color:#fff;font-size:7px;display:flex;align-items:center;justify-content:center;gap:4px}
.btn-login{left:576px;width:57px;background:var(--dark-btn)}
.btn-register{left:638px;width:57px;background:var(--brand-bright)}

/* hero */
.hero{left:0;top:42px;width:782px;height:260px;background:radial-gradient(ellipse at 50% 40%,#8a7a72 0%,#5b4d48 45%,#2d2523 100%)}
.hero-title{left:0;top:86px;width:782px;text-align:center;font-family:"Ubuntu",sans-serif;font-weight:500;font-size:27px;color:#fff}
.hero-sub{left:0;top:116px;width:782px;text-align:center;font-size:9.5px;color:#fff}
.subscribe-field{left:261px;top:136px;width:182px;height:31px;background:#fff;font-size:8px;color:#333;padding:10px 12px}
.subscribe-btn{left:443px;top:136px;width:78px;height:31px;background:var(--brand-bright);color:#fff;font-family:"Ubuntu",sans-serif;font-size:9px;display:flex;align-items:center;justify-content:center;letter-spacing:.3px}
.dots{left:362px;top:240px;display:flex;gap:10px}
.dots span{width:5px;height:5px;border-radius:50%;background:#fff}
.dots span.active{background:none;border:1px solid #fff}

/* section headings */
.heading{font-family:"Ubuntu",sans-serif;font-size:16.5px;color:var(--brand)}

/* categories */
.categories{left:86px;top:369px;width:142px;border-top:1px solid var(--line)}
.categories li{list-style:none;height:36.5px;border-bottom:1px solid var(--line);display:flex;align-items:center;font-size:9px;color:#333}
.categories li svg{width:18px;margin-right:6px}

/* listings */
.event-card{position:absolute;left:246px;width:281px;height:104px;background:#fff;border:1px solid var(--line)}
.event-photo{position:absolute;left:5px;top:5px;width:99px;height:93px}
.event-body{position:absolute;left:114px;top:6px;width:160px}
.event-title{font-size:10px;color:#222;margin-bottom:3px}
.event-desc{font-size:5.2px;line-height:9px;color:var(--muted)}
.event-meta{font-size:5.2px;color:#999;display:flex;align-items:center;gap:5px;margin-top:5px}
.event-meta:first-of-type{margin-top:8px}
.stars{color:#aaa;letter-spacing:1px;font-size:6px}

/* sidebar */
.feature{left:539px;top:369px;width:156px;height:130px;background:linear-gradient(180deg,#b88d5c 0%,#7a5030 45%,#2a1b14 100%)}
.feature-title{left:555px;top:469px;font-size:8.5px;font-weight:600;color:#fff}
.feature-link{left:555px;top:482px;font-size:7px;font-weight:600;color:var(--brand-bright);display:flex;align-items:center;gap:3px}
.speaker-card{left:539px;top:539px;width:156px;height:130px;background:#fff;border:1px solid var(--line)}
.speaker-photo{position:absolute;left:13px;top:13px;width:41px;height:41px;border-radius:50%;background:linear-gradient(135deg,#d6d6d6,#8e8e8e)}
.speaker-name{position:absolute;left:63px;top:20px;font-size:8.5px;color:#333}
.speaker-role{position:absolute;left:63px;top:32px;width:85px;font-size:5.2px;line-height:7px;color:#888}
.speaker-bio{position:absolute;left:16px;top:66px;width:128px;font-size:5.2px;line-height:9px;color:var(--muted)}
.speaker-more{position:absolute;left:16px;top:111px;font-size:5.5px;color:#333;text-decoration:underline}
.social{left:539px;top:715px;display:flex;gap:5px}
.social span{width:16px;height:16px;border-radius:50%}

/* footer */
.site-footer{left:0;top:1158px;width:782px;height:42px;background:var(--footer)}
.footer-nav{left:86px;top:1175px;font-size:6.5px;color:#666}
.footer-nav span{margin:0 4px;color:#999}
.copyright{left:519px;top:1175px;font-size:6.5px;color:#666}
.page-mark{left:764px;top:1186px;font-size:7px;color:#666}
</style>
</head>
<body>

<header class="site-header">
  <div class="abs brand-square"></div>
  <div class="abs brand-name">Vorlume</div>
  <div class="abs search">Search Event
    <svg width="8" height="8" viewBox="0 0 8 8"><circle cx="3.3" cy="3.3" r="2.4" fill="none" stroke="#333" stroke-width="1"/><line x1="5" y1="5" x2="7.5" y2="7.5" stroke="#333" stroke-width="1.1"/></svg>
  </div>
  <div class="abs menu-btn"><svg width="10" height="8" viewBox="0 0 10 8"><rect y="0" width="10" height="1.3" fill="#444"/><rect y="3.3" width="10" height="1.3" fill="#444"/><rect y="6.6" width="10" height="1.3" fill="#444"/></svg></div>
  <div class="abs btn btn-login"><svg width="7" height="7" viewBox="0 0 7 7"><path d="M0 3h4V1.5L6.5 3.5 4 5.5V4H0z" fill="#fff"/></svg>Log in</div>
  <div class="abs btn btn-register"><svg width="7" height="7" viewBox="0 0 7 7"><rect x=".5" y="1" width="5" height="5.5" fill="none" stroke="#fff"/><path d="M3 4l3.5-3.5" stroke="#fff"/></svg>Register</div>
</header>

<section>
  <div class="abs hero" role="img" aria-label="Large audience seated at an event, seen from behind"></div>
  <h1 class="abs hero-title">Welcome to Vorlume</h1>
  <p class="abs hero-sub">Aenean tempus finibus urna, sit amet fermentum diam pharetra</p>
  <div class="abs subscribe-field">Email Address</div>
  <div class="abs subscribe-btn">SUBSCRIBE</div>
  <div class="abs dots"><span class="active"></span><span></span><span></span><span></span></div>
</section>

<h2 class="abs heading" style="left:86px;top:339px">Event categories</h2>
<ul class="abs categories">
  <li><svg viewBox="0 0 10 10" height="8"><path d="M1 5L5 1.5 9 5H8v4H6V6.5H4V9H2V5z" fill="#333"/></svg>Home</li>
  <li><svg viewBox="0 0 10 10" height="8"><path d="M3.5 2L8.5 1v6" stroke="#333" stroke-width="1.2" fill="none"/><path d="M3.5 2v6" stroke="#333" stroke-width="1.2"/><circle cx="2.5" cy="8" r="1.4" fill="#333"/><circle cx="7.5" cy="7" r="1.4" fill="#333"/></svg>Music</li>
  <li><svg viewBox="0 0 10 10" height="8"><rect x="1.5" y="2" width="7" height="5" fill="none" stroke="#333" stroke-width="1.2"/><rect x="0" y="7.5" width="10" height="1.2" fill="#333"/></svg>Technology</li>
  <li><svg viewBox="0 0 10 10" height="8"><rect x="0.5" y="3" width="9" height="4.5" rx="2.2" fill="#333"/><circle cx="7" cy="5.2" r=".8" fill="#fff"/><rect x="2" y="4.8" width="2.4" height=".9" fill="#fff"/></svg>Games</li>
  <li><svg viewBox="0 0 10 10" height="8"><path d="M2 1h6.5l-1 8H1z" fill="#333"/><path d="M2.8 2.6h4.4" stroke="#fff" stroke-width=".7"/></svg>Books</li>
  <li><svg viewBox="0 0 10 10" height="8"><rect x="0.5" y="2.5" width="9" height="6" fill="#333"/><rect x="3.5" y="1" width="3" height="2" fill="none" stroke="#333"/><rect x="0.5" y="5" width="9" height=".6" fill="#fff"/></svg>Business</li>
  <li><svg viewBox="0 0 10 10" height="8"><path d="M4.3 0.5h1.4v2.5h2.3v1.3H5.7V9.5H4.3V4.3H2V3h2.3z" fill="#333"/></svg>Religious</li>
  <li><svg viewBox="0 0 10 10" height="8"><path d="M3.5 1.5L0.5 3l1 2.2 1.2-.5V9h4.6V4.7l1.2.5 1-2.2-3-1.5c-.3.8-1 1.2-1.5 1.2S3.8 2.3 3.5 1.5z" fill="#333"/></svg>Fashion</li>
</ul>

<h2 class="abs heading" style="left:245px;top:339px">Event Listings</h2>

<main>
  <article class="event-card" style="top:369px">
    <div class="event-photo" role="img" aria-label="Young woman seated at a table" style="background:linear-gradient(135deg,#e8e3dc,#cbbfb2 60%,#8c7e74)"></div>
    <div class="event-body">
      <h3 class="event-title" style="font-weight:400">Event Name</h3>
      <p class="event-desc">Cras non ligula pulvinar, posuere magna sed, vehicula ex. Duis rutrum elementum malesuada.</p>
      <div class="event-meta">● 24 Building name, Street name, City- Zipcode</div>
      <div class="event-meta">● Speaker name1,Speaker name2</div>
      <div class="event-meta"><span class="stars">★★★★★</span>- 227 Reviews</div>
      <div class="event-meta">● User</div>
    </div>
  </article>
  <article class="event-card" style="top:478.5px">
    <div class="event-photo" role="img" aria-label="Banquet hall set with dining tables" style="background:linear-gradient(160deg,#cfc4b3,#9a8a73 60%,#6b5c4a)"></div>
    <div class="event-body">
      <h3 class="event-title" style="font-weight:400">Mauris eu ligula in sapien</h3>
      <p class="event-desc">Cras non ligula pulvinar, posuere magna sed, vehicula ex. Duis rutrum elementum malesuada.</p>
      <div class="event-meta">● 24 Building name, Street name, City- Zipcode</div>
      <div class="event-meta">● William, Sophia, Stuart</div>
      <div class="event-meta"><span class="stars">★★★★★</span>- 227 Reviews</div>
      <div class="event-meta">● John Cole</div>
    </div>
  </article>
  <article class="event-card" style="top:588px">
    <div class="event-photo" role="img" aria-label="Festival gathering in the mountains with prayer flags" style="background:linear-gradient(180deg,#c9c8c6,#8f8576 55%,#6d4b3a)"></div>
    <div class="event-body">
      <h3 class="event-title" style="font-weight:400">Mauris eu ligula in sapien</h3>
      <p class="event-desc">Cras non ligula pulvinar, posuere magna sed, vehicula ex. Duis rutrum elementum malesuada.</p>
      <div class="event-meta">● 24 Building name, Street name, City- Zipcode</div>
      <div class="event-meta">● William, Sophia, Stuart</div>
      <div class="event-meta"><span class="stars">★★★★★</span>- 227 Reviews</div>
      <div class="event-meta">● John Cole</div>
    </div>
  </article>
  <article class="event-card" style="top:697.5px">
    <div class="event-photo" role="img" aria-label="Trade show booth with visitors" style="background:linear-gradient(135deg,#1d3f78,#2d6a8a 50%,#1a1e28)"></div>
    <div class="event-body">
      <h3 class="event-title" style="font-weight:400">Mauris eu ligula in sapien</h3>
      <p class="event-desc">Cras non ligula pulvinar, posuere magna sed, vehicula ex. Duis rutrum elementum malesuada.</p>
      <div class="event-meta">● 24 Building name, Street name, City- Zipcode</div>
      <div class="event-meta">● William, Sophia, Stuart</div>
      <div class="event-meta"><span class="stars">★★★★★</span>- 227 Reviews</div>
      <div class="event-meta">● John Cole</div>
    </div>
  </article>
  <article class="event-card" style="top:807px">
    <div class="event-photo" role="img" aria-label="Concert crowd with raised hands under stage lights" style="background:radial-gradient(circle at 50% 30%,#f5e4c8,#b8876a 40%,#3b2a3e 80%)"></div>
    <div class="event-body">
      <h3 class="event-title" style="font-weight:400">Mauris eu ligula in sapien</h3>
      <p class="event-desc">Cras non ligula pulvinar, posuere magna sed, vehicula ex. Duis rutrum elementum malesuada.</p>
      <div class="event-meta">● 24 Building name, Street name, City- Zipcode</div>
      <div class="event-meta">● William, Sophia, Stuart</div>
      <div class="event-meta"><span class="stars">★★★★★</span>- 227 Reviews</div>
      <div class="event-meta">● John Cole</div>
    </div>
  </article>
  <article class="event-card" style="top:916.5px">
    <div class="event-photo" role="img" aria-label="Performer in a hat under coloured lights" style="background:linear-gradient(135deg,#2f6e8e,#27304f 50%,#c58a3b)"></div>
    <div class="event-body">
      <h3 class="event-title" style="font-weight:400">Mauris eu ligula in sapien</h3>
      <p class="event-desc">Cras non ligula pulvinar, posuere magna sed, vehicula ex. Duis rutrum elementum malesuada.</p>
      <div class="event-meta">● 24 Building name, Street name, City- Zipcode</div>
      <div class="event-meta">● William, Sophia, Stuart</div>
      <div class="event-meta"><span class="stars">★★★★★</span>- 227 Reviews</div>
      <div class="event-meta">● John Cole</div>
    </div>
  </article>
  <article class="event-card" style="top:1026px">
    <div class="event-photo" role="img" aria-label="Motor show hall with cars and visitors" style="background:linear-gradient(180deg,#3b3a3d,#6d6468 55%,#b7232f)"></div>
    <div class="event-body">
      <h3 class="event-title" style="font-weight:400">Mauris eu ligula in sapien</h3>
      <p class="event-desc">Cras non ligula pulvinar, posuere magna sed, vehicula ex. Duis rutrum elementum malesuada.</p>
      <div class="event-meta">● 24 Building name, Street name, City- Zipcode</div>
      <div class="event-meta">● William, Sophia, Stuart</div>
      <div class="event-meta"><span class="stars">★★★★★</span>- 227 Reviews</div>
      <div class="event-meta">● John Cole</div>
    </div>
  </article>
</main>

<aside>
  <div class="abs feature" role="img" aria-label="Conference auditorium filled with attendees"></div>
  <div class="abs feature-title">Aenean tempus finibus urna</div>
  <div class="abs feature-link"><svg width="7" height="7" viewBox="0 0 7 7"><path d="M0 3.5L3.5 0H7v3.5L3.5 7z" fill="#0aa2ef"/><circle cx="5" cy="2" r=".7" fill="#fff"/></svg>BUY TICKETS</div>

  <h2 class="abs heading" style="left:539px;top:514px">Speaker of this month</h2>
  <div class="abs speaker-card">
    <div class="speaker-photo" role="img" aria-label="Speaker portrait"></div>
    <div class="speaker-name">William</div>
    <div class="speaker-role">Pellentesque habitant morbi tristique senectus</div>
    <p class="speaker-bio">Aenean mi diam, rhoncus et vestibulum et, accumsan ac justo. Cras orci leo, tempor vel euismod vel, varius sed nibh. Praesent placer- at tincidunt mi, sit amet ultrices tellus</p>
    <div class="speaker-more">Read More</div>
  </div>

  <h2 class="abs heading" style="left:539px;top:686px">Share us on</h2>
  <div class="abs social">
    <span style="background:#3b5998"></span>
    <span style="background:#1da1f2"></span>
    <span style="background:#0077b5"></span>
    <span style="background:#dd4b39"></span>
    <span style="background:#cb2027"></span>
    <span style="background:#f57d00"></span>
    <span style="background:#e52d27"></span>
  </div>
</aside>

<footer>
  <div class="abs site-footer"></div>
  <div class="abs footer-nav">Home<span>|</span>About<span>|</span>Event Categories<span>|</span>Reviews<span>|</span>Speakers<span>|</span>Locations<span>|</span>Search</div>
  <div class="abs copyright">Copyright © 2017 Company name. All rights reserved.</div>
  <div class="abs page-mark">M2</div>
</footer>

</body>
</html>
```